Take my logo and make me some cool looking business cards

I've got a logo that we've trademarked so you can't change the logo but you can change it's color combo and find a fun way to incorporate it into a new business card design that is fresh, stylish, and can be applied to some cool medium cost materials (plastic, wood, metal, etc). Basically, we're looking for business cards that stand out in a good way.
Here's the logo we're currently using:
Thanks to everyone that has submitted designs. We've narrowed down to the top 4 designs and tried to eliminate old versions or designs that just didn't match our vision as quickly as we could. We don't plan on keeping this open for the full 9 days; we plan on selecting a design in the next 48 hours; with the goal of having something in the hands of a printer, preferably plastic printer, by Thursday AM Pacific Time.
Business
- must include our existing logo

```html
<!DOCTYPE html>
<html lang="en">
<head>
<meta charset="utf-8">
<title>Tidewell Business Card</title>
<link rel="stylesheet" href="https://fonts.googleapis.com/css2?family=Nunito+Sans:wght@400;600&display=swap">
<style>
  :root {
    --stage: #2a2a2c;
    --card-white: #f7f7f8;
    --card-navy: #243c55;
    --navy-soft: #2f4b68;
    --brand-blue: #2aa6d3;
    --ink: #2b3a4d;
    --icon: #2aa6d3;
    --light: #ffffff;
  }
  * { box-sizing: border-box; margin: 0; padding: 0; }
  html, body { width: 1200px; height: 900px; overflow: hidden; }
  body {
    background: var(--stage);
    font-family: "Nunito Sans", Arial, sans-serif;
    display: flex;
    align-items: center;
    justify-content: center;
    gap: 40px;
  }
  .card {
    width: 540px;
    height: 310px;
    border-radius: 22px;
    position: relative;
    overflow: hidden;
  }
  .card--back {
    background: var(--card-navy);
  }
  .back-pattern {
    position: absolute;
    inset: 0;
    background: linear-gradient(135deg, var(--navy-soft), var(--card-navy));
  }
  .back-wordmark {
    position: absolute;
    right: 48px;
    top: 118px;
    font-size: 34px;
    font-weight: 600;
    letter-spacing: 3px;
    color: var(--light);
  }
  .card--front {
    background: var(--card-white);
  }
  .front-wordmark {
    position: absolute;
    left: 38px;
    top: 130px;
    font-size: 38px;
    font-weight: 600;
    letter-spacing: 3px;
    color: var(--brand-blue);
  }
  .contact {
    position: absolute;
    left: 318px;
    top: 88px;
    color: var(--ink);
  }
  .contact__name {
    font-size: 22px;
    font-weight: 600;
    line-height: 1.1;
  }
  .contact__role {
    font-size: 14px;
    margin: 2px 0 12px 8px;
  }
  .contact__list { list-style: none; margin-left: 20px; }
  .contact__item {
    display: flex;
    align-items: flex-start;
    gap: 6px;
    font-size: 15px;
    line-height: 1.3;
    margin-bottom: 2px;
  }
  .contact__item svg { width: 13px; height: 13px; margin-top: 3px; flex: none; fill: var(--icon); }
</style>
</head>
<body>
  <section class="card card--back">
    <div class="back-pattern" role="img" aria-label="Repeating brand mark pattern in muted navy"></div>
    <div class="back-wordmark">TIDEWELL</div>
  </section>

  <section class="card card--front">
    <div class="front-wordmark">TIDEWELL</div>
    <div class="contact">
      <p class="contact__name">Jordan Reyes</p>
      <p class="contact__role">CEO</p>
      <ul class="contact__list">
        <li class="contact__item">
          <svg viewBox="0 0 12 12" aria-hidden="true"><path d="M3 0h6a1 1 0 0 1 1 1v10a1 1 0 0 1-1 1H3a1 1 0 0 1-1-1V1a1 1 0 0 1 1-1zm0 1.5v8h6v-8z"/></svg>
          <span>+1 5550 123 456</span>
        </li>
        <li class="contact__item">
          <svg viewBox="0 0 12 12" aria-hidden="true"><path d="M0 2h12v8H0zM1 3l5 3.5L11 3z" fill-rule="evenodd"/></svg>
          <span>jr@tidewell.com</span>
        </li>
        <li class="contact__item">
          <svg viewBox="0 0 12 12" aria-hidden="true"><path d="M6 0a4 4 0 0 1 4 4c0 3-4 8-4 8S2 7 2 4a4 4 0 0 1 4-4zm0 2.5a1.5 1.5 0 1 0 0 3 1.5 1.5 0 0 0 0-3z"/></svg>
          <span>412 Harbor Lane<br>Seacliff, CA 90000</span>
        </li>
      </ul>
    </div>
  </section>
</body>
</html>
```